New business card design needed for Trucking/Staffing company!

I am looking for a business card design. The business name is Harbor Lane Freightworks, LLC. This company is a staffing company for commercial drivers/truck drivers. Most of our customers are trucking/supply companies. Our colors are blue/black/white/grey. The info I have on my current business cards is
-Spot for a name
-2 lines for an address
-3 lines for Office, cell, and fax
-email
-website(currently on backside of card with logo but can go anywhere)
Updates

Project Deadline Extended
Reason: Open to more designs

Target Market(s)

Trucking companies, building supply companies

Industry/Entity Type

Business

Contact Information for Business Card

Edgy but professional

Font styles to use
Other font styles liked:
• Open to suggestions

Colors
0555a3
000000
ffffff
9d9d9d

Requirements
Must have
• Must have the logo incorporated

```html
<!DOCTYPE html>
<html lang="en">
<head>
<meta charset="utf-8">
<title>Harbor Lane Freightworks – Business Card</title>
<link href="https://fonts.googleapis.com/css2?family=Lato:wght@400;700;900&display=swap" rel="stylesheet">
<style>
  :root {
    --brand-blue: #3a3fae;
    --brand-blue-deep: #2a2e86;
    --charcoal: #333436;
    --charcoal-light: #3d3e40;
    --paper: #ffffff;
    --paper-shade: #f2f2f2;
    --ink: #3a3a3a;
    --ink-soft: #7a7a7a;
    --backdrop: #e6e6e6;
  }
  * { margin: 0; padding: 0; box-sizing: border-box; }
  html, body { width: 1200px; height: 800px; overflow: hidden; }
  body {
    background: var(--backdrop);
    font-family: "Lato", sans-serif;
    position: relative;
  }
  .card {
    position: absolute;
    top: 250px;
    width: 520px;
    height: 300px;
    background: linear-gradient(180deg, var(--paper), var(--paper-shade));
    box-shadow: 0 10px 28px rgba(0,0,0,0.22);
    overflow: hidden;
  }
  .card--front { left: 50px; }
  .card--back { left: 630px; }
  .card-shapes { position: absolute; inset: 0; }

  .wordmark {
    position: absolute;
    left: 110px;
    top: 62px;
    width: 320px;
    display: flex;
    align-items: center;
    gap: 12px;
  }
  .wordmark-square {
    width: 22px; height: 22px;
    background: var(--brand-blue);
    flex: none;
  }
  .wordmark-name {
    font-weight: 900;
    font-size: 24px;
    line-height: 1.1;
    letter-spacing: 1px;
    color: var(--brand-blue);
    text-transform: uppercase;
  }

  .holder {
    position: absolute;
    left: 30px;
    top: 40px;
    display: flex;
    align-items: center;
    gap: 10px;
  }
  .holder-name {
    font-size: 18px;
    font-weight: 400;
    letter-spacing: 0.5px;
    color: var(--ink);
  }
  .holder-role {
    font-size: 13px;
    color: var(--ink-soft);
  }

  .contact {
    position: absolute;
    color: var(--paper);
    font-size: 11.5px;
    line-height: 15px;
    letter-spacing: 0.3px;
  }
  .contact--phones { left: 22px; top: 240px; }
  .contact--web { left: 175px; top: 208px; text-align: center; width: 170px; }
  .contact--address { right: 18px; top: 160px; text-align: right; }
</style>
</head>
<body>

  <section class="card card--front" aria-label="Card front">
    <svg class="card-shapes" viewBox="0 0 520 300" width="520" height="300">
      <polygon points="0,228 520,148 520,300 0,300" fill="var(--charcoal)"/>
      <polygon points="0,198 520,118 520,148 0,228" fill="var(--brand-blue)"/>
      <polygon points="470,126 520,118 520,148 470,156" fill="var(--brand-blue-deep)"/>
      <polygon points="0,198 30,193 30,223 0,228" fill="var(--brand-blue-deep)"/>
    </svg>
    <div class="wordmark">
      <span class="wordmark-square"></span>
      <span class="wordmark-name">Harbor Lane Freightworks, LLC</span>
    </div>
  </section>

  <section class="card card--back" aria-label="Card back">
    <svg class="card-shapes" viewBox="0 0 520 300" width="520" height="300">
      <polygon points="0,245 520,150 520,300 0,300" fill="var(--charcoal)"/>
      <polygon points="0,215 520,120 520,150 0,245" fill="var(--brand-blue)"/>
      <polygon points="480,127 520,120 520,150 480,157" fill="var(--brand-blue-deep)"/>
      <polygon points="0,215 35,209 35,239 0,245" fill="var(--brand-blue-deep)"/>
      <line x1="40" y1="222.7" x2="490" y2="140.5" stroke="var(--paper)" stroke-width="1"/>

      <!-- phone -->
      <g transform="translate(70,217.2)">
        <circle r="12" fill="var(--brand-blue)" stroke="var(--paper)" stroke-width="1.5"/>
        <path d="M-5,-5 q2,-2 3,0 l1,2 q0,1.5 -1.5,2 q1,2.5 3.5,3.5 q0.5,-1.5 2,-1.5 l2,1 q2,1 0,3 q-2,2 -5,0.5 q-4,-2 -6,-6 q-1.5,-3 1,-4.5z" fill="var(--paper)"/>
      </g>
      <!-- globe -->
      <g transform="translate(260,182.5)" fill="none" stroke="var(--paper)" stroke-width="1.3">
        <circle r="12" fill="var(--brand-blue)" stroke-width="1.5"/>
        <circle r="7"/>
        <ellipse rx="3" ry="7"/>
        <line x1="-7" y1="0" x2="7" y2="0"/>
        <line x1="-6" y1="-3.5" x2="6" y2="-3.5"/>
        <line x1="-6" y1="3.5" x2="6" y2="3.5"/>
      </g>
      <!-- home -->
      <g transform="translate(450,147.8)">
        <circle r="12" fill="var(--brand-blue)" stroke="var(--paper)" stroke-width="1.5"/>
        <path d="M-6,0 L0,-6 L6,0 M-4,-1 V5 H4 V-1" fill="none" stroke="var(--paper)" stroke-width="1.5"/>
        <rect x="-1.2" y="1.5" width="2.4" height="3.5" fill="var(--paper)"/>
      </g>
    </svg>

    <div class="holder">
      <svg width="36" height="36" viewBox="0 0 36 36" aria-hidden="true">
        <circle cx="18" cy="18" r="18" fill="var(--brand-blue)"/>
        <circle cx="18" cy="14" r="5.5" fill="var(--paper)"/>
        <path d="M8,27 q10,-12 20,0z" fill="var(--paper)"/>
      </svg>
      <div>
        <div class="holder-name">DANIEL REYES</div>
        <div class="holder-role">Managing Director</div>
      </div>
    </div>

    <div class="contact contact--phones">
      <div>Office: +0912-48-73-20</div>
      <div>Cell: 555-210-447-3</div>
      <div>Fax: 555-210-447-9</div>
    </div>
    <div class="contact contact--web">
      <div>d.reyes@harborlane.com</div>
      <div>www.harborlanefreight.com</div>
    </div>
    <div class="contact contact--address">
      <div>Address Line 1</div>
      <div>Address Line 2</div>
    </div>
  </section>

</body>
</html>
```